Meadowlark Learning Growth Partners (MLGP)

This is a professional business card. Logo and picture are a must on the front of the card. I am an educational consultant. I have been consulting for the past three years for a company. I am now opening my own company. My goal for my consulting company is to eventually consult all over America.

Target Market(s)

Educators, schools, professionals

Industry/Entity Type

Consulting

Contact Information for Business Card

Picture/logo on front, simple modern design

Font styles to use
Serif

Colors
85abd2
0355a3
3176b5
cedeed

Requirements
Must have
• picture, logo,
• Odessa Pruitt, Ed.S
• address 5073 Cormorant ridge Dr. Nashville, TN 37940
• Cell:616-555-0148
• Office: 629-555-0172
• www.Mlgpedu.example
• pruittodessa@mailbox.example

```html
<!DOCTYPE html>
<html lang="en">
<head>
<meta charset="UTF-8">
<title>Meadowlark Learning Growth Partners — Business Card</title>
<link rel="stylesheet" href="https://fonts.googleapis.com/css2?family=Montserrat+Alternates:wght@700&family=Roboto:wght@400&display=swap">
<style>
  :root {
    --navy: #053a7a;
    --white: #ffffff;
    --backdrop: #2b2b2b;
    --photo-tone-a: #3f7fd0;
    --photo-tone-b: #1d4f9a;
  }
  * { margin: 0; padding: 0; box-sizing: border-box; }
  html, body { width: 1200px; height: 900px; overflow: hidden; background: var(--backdrop); }
  .card {
    position: absolute; left: 250px; width: 700px; height: 400px;
    background: var(--white); overflow: hidden;
    box-shadow: 0 10px 30px rgba(0,0,0,.5);
  }
  .card--front { top: 40px; }
  .card--back { top: 460px; }
  .card__wave { position: absolute; inset: 0; }
  .brand { position: absolute; display: flex; align-items: center; color: var(--navy);
    font-family: "Montserrat Alternates", sans-serif; font-weight: 700; }
  .brand__dot { border-radius: 50%; background: var(--navy); flex: none; }
  .brand__short { letter-spacing: 2px; }
  .brand__rule { background: var(--navy); align-self: stretch; flex: none; }
  .brand__full { line-height: 1.05; }
  .card--front .brand { left: 100px; top: 60px; }
  .card--front .brand__dot { width: 44px; height: 44px; margin-right: 16px; }
  .card--front .brand__short { font-size: 46px; margin-right: 18px; }
  .card--front .brand__rule { width: 2px; margin-right: 16px; }
  .card--front .brand__full { font-size: 22px; }
  .card--back .brand { left: 40px; top: 70px; }
  .card--back .brand__dot { width: 26px; height: 26px; margin-right: 10px; }
  .card--back .brand__short { font-size: 26px; margin-right: 10px; }
  .card--back .brand__rule { width: 1.5px; margin-right: 9px; }
  .card--back .brand__full { font-size: 12px; }
  .web-front { position: absolute; right: 30px; top: 245px; color: var(--white);
    font-family: "Roboto", sans-serif; font-size: 15px; }
  .portrait { position: absolute; left: 515px; top: 35px; width: 112px; height: 128px;
    border: 3px solid var(--navy);
    background: linear-gradient(160deg, var(--photo-tone-a), var(--photo-tone-b)); }
  .person { position: absolute; left: 480px; top: 172px; width: 180px; text-align: center;
    color: var(--navy); font-family: "Montserrat Alternates", sans-serif; font-weight: 700; }
  .person__name { font-size: 18px; }
  .person__title { font-family: "Roboto", sans-serif; font-weight: 400; font-size: 12px; }
  .contacts { position: absolute; left: 50px; top: 298px; list-style: none;
    color: var(--white); font-family: "Roboto", sans-serif; font-size: 14px; }
  .contacts li { display: flex; align-items: center; height: 18px; }
  .contacts svg { width: 13px; height: 13px; margin-right: 10px; fill: var(--white); flex: none; }
</style>
</head>
<body>

<section class="card card--front">
  <svg class="card__wave" viewBox="0 0 700 400" aria-hidden="true">
    <path d="M0,335 C200,330 330,300 420,240 C500,190 590,165 700,158 L700,400 L0,400 Z" fill="var(--navy)"/>
    <path d="M0,360 C210,355 340,322 430,262 C510,212 600,190 690,184" fill="none" stroke="var(--white)" stroke-width="3"/>
    <path d="M0,378 C220,372 345,338 435,282" fill="none" stroke="var(--white)" stroke-width="6"/>
  </svg>
  <div class="brand">
    <span class="brand__dot"></span>
    <span class="brand__short">MLGP</span>
    <span class="brand__rule"></span>
    <span class="brand__full">Meadowlark<br>Learning<br>Growth<br>Partners</span>
  </div>
  <div class="web-front">www.Mlgpedu.example</div>
</section>

<section class="card card--back">
  <svg class="card__wave" viewBox="0 0 700 400" aria-hidden="true">
    <path d="M0,285 C120,250 260,245 420,242 C560,238 650,225 700,170 L700,400 L0,400 Z" fill="var(--navy)"/>
    <path d="M70,286 C170,264 290,258 430,255 C570,251 655,238 700,193" fill="none" stroke="var(--white)" stroke-width="2.5"/>
    <path d="M520,228 C600,222 660,205 700,178 L700,176 C650,200 590,215 520,228 Z" fill="var(--white)"/>
  </svg>
  <div class="brand">
    <span class="brand__dot"></span>
    <span class="brand__short">MLGP</span>
    <span class="brand__rule"></span>
    <span class="brand__full">Meadowlark<br>Learning<br>Growth<br>Partners</span>
  </div>
  <div class="portrait" role="img" aria-label="Portrait photo of Odessa Pruitt"></div>
  <div class="person">
    <div class="person__name">Odessa Pruitt</div>
    <div class="person__title">Ed.S</div>
  </div>
  <ul class="contacts">
    <li><svg viewBox="0 0 16 16"><path d="M3 1l3 3-2 2c1 2 3 4 5 5l2-2 3 3-2 3C6 15 1 10 0 4z"/></svg>616-555-0148</li>
    <li><svg viewBox="0 0 16 16"><path d="M1 5c4-3 10-3 14 0v2h-4V5H5v2H1zM3 8h10l1 7H2z"/></svg>629-555-0172</li>
    <li><svg viewBox="0 0 16 16"><path d="M0 3h16v10H0zM1 4l7 5 7-5v-.5H1z"/></svg>pruittodessa@mailbox.example</li>
    <li><svg viewBox="0 0 16 16"><circle cx="8" cy="8" r="7" fill="none" stroke="#fff" stroke-width="1.5"/><path d="M1 8h14M8 1c-3 4-3 10 0 14M8 1c3 4 3 10 0 14" fill="none" stroke="#fff" stroke-width="1.2"/></svg>www.Mlgpedu.example</li>
    <li><svg viewBox="0 0 16 16"><path d="M8 0a5.5 5.5 0 0 0-5.5 5.5C2.5 10 8 16 8 16s5.5-6 5.5-10.5A5.5 5.5 0 0 0 8 0zm0 8a2.5 2.5 0 1 1 0-5 2.5 2.5 0 0 1 0 5z"/></svg>5073 Cormorant ridge Dr. Nashville, TN 37940</li>
  </ul>
</section>

</body>
</html>
```